Design a New Business Card for Our Company

We are looking for fresh, unique, and a modern business card that reflects our roots as digital marketing agency focused on SEM.

Industry/Entity Type

Marketing

Contact Information for Business Card

looking for very unique out of the box designs. clean and modern that compliments our logo

Requirements
Must have
• colors should match our logo
• Front should have name, address, email, and phone/fax of the person, phone/fax are the same number
• back should have our url

```html
<!DOCTYPE html>
<html lang="en">
<head>
<meta charset="utf-8">
<title>Northgate Solutions – Business Card</title>
<link rel="stylesheet" href="https://fonts.googleapis.com/css2?family=Nunito+Sans:wght@400;600;700;800&display=swap">
<style>
  :root {
    --page-bg: #d9d4cd;
    --card-bg: #eef0f1;
    --card-edge: #c9cccf;
    --text-grey: #7b7d80;
    --brand-blue: #3f6ea8;
    --brand-grey: #8a8a8a;
    --deco-grey: #9a9896;
  }
  * { margin: 0; padding: 0; box-sizing: border-box; }
  html, body {
    width: 1200px;
    height: 970px;
    overflow: hidden;
    background: var(--page-bg);
    font-family: "Nunito Sans", Arial, sans-serif;
  }
  .card {
    position: absolute;
    left: 100px;
    top: 201px;
    width: 1000px;
    height: 568px;
    background: linear-gradient(160deg, #f4f5f6 0%, var(--card-bg) 60%, #e6e8ea 100%);
    border: 1px solid var(--card-edge);
    box-shadow: 0 10px 30px rgba(0,0,0,0.12);
    overflow: hidden;
  }
  .brand {
    position: absolute;
    left: 50px;
    top: 92px;
    display: flex;
    align-items: center;
    gap: 16px;
  }
  .brand-dot {
    width: 56px;
    height: 56px;
    border-radius: 50%;
    background: var(--brand-blue);
    flex: none;
  }
  .brand-name {
    font-size: 44px;
    font-weight: 800;
    color: var(--brand-blue);
    letter-spacing: -0.5px;
    line-height: 1;
    white-space: nowrap;
  }
  .person {
    position: absolute;
    left: 50px;
    top: 254px;
  }
  .person-name {
    font-size: 31px;
    font-weight: 800;
    color: var(--brand-blue);
    line-height: 1.1;
  }
  .person-role {
    font-size: 22px;
    font-weight: 600;
    color: var(--text-grey);
  }
  .address {
    position: absolute;
    left: 50px;
    top: 355px;
    font-size: 26px;
    color: var(--text-grey);
    line-height: 1.4;
    font-style: normal;
  }
  .contacts {
    position: absolute;
    left: 50px;
    top: 438px;
    list-style: none;
    font-size: 26px;
    color: var(--text-grey);
  }
  .contacts li {
    display: flex;
    align-items: center;
    gap: 6px;
    height: 35px;
    white-space: nowrap;
  }
  .contacts svg { width: 28px; height: 28px; flex: none; }
  .decoration {
    position: absolute;
    right: 0;
    top: 0;
    width: 370px;
    height: 100%;
    background: radial-gradient(circle at 60% 45%, rgba(154,152,150,0.55) 0%, rgba(63,110,168,0.35) 55%, rgba(238,240,241,0) 85%);
  }
</style>
</head>
<body>
  <main class="card">
    <div class="brand">
      <span class="brand-dot"></span>
      <span class="brand-name">Northgate Solutions</span>
    </div>

    <div class="person">
      <div class="person-name">ALEX CARTER</div>
      <div class="person-role">Maneger</div>
    </div>

    <address class="address">
      48 Harbor Lane, 2nd Ste<br>
      Ridgefield, Texas 75301
    </address>

    <ul class="contacts">
      <li>
        <svg viewBox="0 0 28 28" aria-hidden="true"><rect width="28" height="28" fill="#3f6ea8"/><path d="M7 9c2-3 4-3 4-1l1 3-2 1c1 2 3 4 5 5l1-2 3 1c2 0 2 2-1 4-5 1-12-6-11-11z" fill="#fff"/></svg>
        214 555 0187
      </li>
      <li>
        <svg viewBox="0 0 28 28" aria-hidden="true"><rect width="28" height="28" fill="#3f6ea8"/><rect x="8" y="5" width="12" height="7" fill="#fff"/><rect x="5" y="12" width="18" height="10" fill="#fff"/><rect x="9" y="16" width="10" height="2" fill="#3f6ea8"/></svg>
        214 555 0187
      </li>
      <li>
        <svg viewBox="0 0 28 28" aria-hidden="true"><rect width="28" height="28" fill="#3f6ea8"/><rect x="5" y="8" width="18" height="13" fill="#fff"/><path d="M5 8l9 7 9-7" fill="none" stroke="#3f6ea8" stroke-width="1.6"/></svg>
        alex@northgate.com
      </li>
    </ul>

    <div class="decoration" role="img" aria-label="Decorative area of scattered grey and blue dots"></div>
  </main>
</body>
</html>
```